Modern Website For Law Firm Lawyer Melbourne, Australia Coded

We are looking for a modern and sophisticated website design. We would prefer the site to be based on WordPress given it is intuitive and some of our staff have experience using it.

Our law firm is based in Melbourne, Australia and we deal with property. The website must be hosted on a reliable Australian server.

We would also appreciate it if the designer can provide some guidance about how to make changes/upload content, such as photos and articles. We are happy to pay for this advice.

We prefer classic fonts in black or grey. We would also like a dash of colour so please use a green, blue or aqua colour palette that is consistent with our logo attached.

We do not want any law related images - scales of justice, gavel or the like.

Our ultimate goal is to communicate that the firm is professional, affordable, modern, dynamic, knowledgeable and one with the community.

We would like the following pages/sections/icons:

1. Who We Are - we will provide content.

2. Our Services - 1. Property 2. Wills, 3. Powers of Attorney 4. Probate & Estate Administration 5.Consultancy & Agency- we will provide content for each of these sections.

3. Articles - we already have approximately 20 articles on a wordpress blog and would like to port these articles to the website. We can do this ourselves if the designer can give us instructions about how to do this. We would also like to give clients the option to subscribe to our articles.

4. Contact Us - this should include our firms contact details; location map and we would like to give clients the option to "Request A Quote" directly from the page - i.e they will need to provide their full name, phone number email address, choose subject from drop down menu and type a message that gets sent to our outlook email.

5. Terms and Conditions - we will provide content

We really like the style and photographs used in the following website and want something as close to this as possible:

https://www.velbrook.com/

For privacy reasons, we would prefer to provide content together with all business details once we have decided on the winner.

We will monitor entries closely and promise to provide feedback and guidance on each entry.

This project is guaranteed. If our budget is too low please email us so we can discuss further and perhaps increase our budget. We are reasonable in this regard.

Thank you very much for considering this project.

Target Market(s)

General public, professionals, lawyers and conveyancers

Industry/Entity Type

Law Firm

Coding

Coded - Design and coding required

Number of Pages Required

1 page

Font styles to use
Sans Serif

Colors
33b8a4
33a6d7
0692cd
3176b5
00a990
9bcb3c
86cfc6
cadf82
85acd3

Requirements
Must have
• 1. Site must be coded and hosted on a reliable Australian server and it would be much appreciated if the deisgner provides instructions about how to add photos, blog articles etc-
• 2. The site must be secure and have green lock at top of page
• 3. Request A Quote - name, email, phone, drop down subject, message - email to our outlook email
• 4. Article Subscription
• 5. Domain (we have already purchased)
• 6. Location map
• 7. Facebook, LinkedIn, Instagram Icons
• 8. Membership icons in this order - KRT Member > Coastal Female Advocates > Guides From Counsel > Creature Foundation > Dorvo > Malpeth > Kel QR logos attached to go on bottom of page
• 9. Testimonials
Nice to have
• A modern, sophisticated website like:
• https://www.velbrook.com/ - we really like the style of the velbrook photographs
• We also really like this design by Tk of Sketch hive:
• https://www.sketchhive.com.au/design/58201346
Should not have
• Law related images - scales of justice gavel and the like

```html
<!DOCTYPE html>
<html lang="en">
<head>
<meta charset="utf-8">
<title>Larkfield Lawyers</title>
<link rel="stylesheet" href="https://fonts.googleapis.com/css2?family=Open+Sans:wght@300;400;600;700&display=swap">
<style>
:root{
  --teal:#33b8a4;
  --aqua:#33a6d7;
  --blue:#0692cd;
  --deep:#3176b5;
  --green:#9bcb3c;
  --ink:#2b2b2b;
  --grey:#555;
  --soft:#8a8a8a;
  --line:#dcdcdc;
  --white:#fff;
  --band:linear-gradient(180deg,#32b5a6 0%,#33aabf 55%,#2f9fd6 100%);
}
*{margin:0;padding:0;box-sizing:border-box}
html,body{width:1200px;height:3622px;overflow:hidden;background:var(--white)}
body{font-family:"Open Sans",Arial,sans-serif;color:var(--ink);position:relative}
section,header,footer{position:absolute;left:0;width:1200px}
.abs{position:absolute}
.section-title{position:absolute;left:0;width:1200px;text-align:center;font-weight:300;font-size:26px;letter-spacing:1px;text-transform:uppercase}
.title-rule{position:absolute;left:588px;width:24px;height:3px;border-radius:2px;background:var(--aqua)}
.on-band .section-title{color:var(--white)}
.on-band .title-rule{background:rgba(255,255,255,.7)}

/* header */
.site-header{top:0;height:106px;background:var(--white)}
.brand{left:145px;top:24px;display:flex;align-items:center;gap:12px}
.brand-dot{width:56px;height:56px;border-radius:50%;background:var(--aqua)}
.brand-name{font-size:19px;font-weight:600;color:var(--ink);line-height:22px;text-transform:uppercase;letter-spacing:.5px}
.top-info{right:145px;top:12px;display:flex;align-items:center;gap:28px;font-size:12px;color:var(--grey)}
.top-info span{display:flex;align-items:center;gap:7px}
.top-info .phone{font-size:19px;font-weight:600;color:var(--ink)}
.main-nav{right:145px;top:58px;display:flex;gap:26px;font-size:12.5px;color:var(--grey)}
.main-nav a{color:inherit;text-decoration:none}
.main-nav .current{color:var(--teal);border-bottom:2px solid var(--teal);padding-bottom:4px}

/* hero */
.hero{top:106px;height:459px}
.hero-photo{position:absolute;inset:0;background:linear-gradient(120deg,#c9d2d8 0%,#e7e0d8 35%,#a8b6c2 65%,#d8dde2 100%)}
.hero-caption{position:absolute;left:0;top:352px;width:1200px;text-align:center;color:var(--white);font-size:29px;font-weight:600;letter-spacing:1.5px;line-height:37px;text-transform:uppercase;text-shadow:0 2px 6px rgba(0,0,0,.45)}

/* who we are */
.who{top:565px;height:473px}
.who-lead{top:128px;left:0;width:1200px;text-align:center;font-size:15px;color:var(--grey)}
.who-photo{left:142px;top:166px;width:394px;height:247px;background:linear-gradient(135deg,#2a2f36,#6b7480 55%,#c9ccd0)}
.who-copy{left:579px;top:174px;width:478px;font-size:13.5px;line-height:22.6px;color:var(--grey);text-align:justify}
.btn{display:inline-block;background:var(--teal);color:var(--white);font-size:12px;font-weight:600;border-radius:16px;padding:7px 22px;letter-spacing:.5px}
.who .btn{position:absolute;left:579px;top:381px}

/* services */
.services{top:1038px;height:439px;background:var(--band)}
.service{position:absolute;top:178px;width:180px;text-align:center;color:var(--white)}
.service-icon{width:88px;height:88px;margin:0 auto;border-radius:50%;background:var(--white);border:4px solid rgba(255,255,255,.45);background-clip:padding-box;display:flex;align-items:center;justify-content:center}
.service h3{margin-top:28px;font-size:13px;font-weight:400;line-height:19px;text-transform:uppercase;height:38px}
.service p{margin-top:12px;font-size:11.5px;line-height:16px;opacity:.9}

/* testimonials */
.testimonials{top:1477px;height:483px}
.arrow{position:absolute;width:30px;height:54px}
.person{position:absolute;top:167px;width:290px;text-align:center}
.avatar{width:74px;height:74px;margin:0 auto;border-radius:50%;border:3px solid #e5e5e5;background:linear-gradient(160deg,#d9c4b6,#8c7b72)}
.person h4{margin-top:18px;font-size:12px;font-weight:400;color:var(--grey);text-transform:uppercase}
.quote-card{position:absolute;top:309px;width:288px;height:114px;border:1px solid var(--line);box-shadow:0 2px 5px rgba(0,0,0,.08);padding:14px 18px;font-size:13px;line-height:20px;color:var(--grey)}
.quote-card.active{border-color:var(--teal)}
.qm{color:#bbb;font-weight:700;font-size:17px}

/* articles */
.articles{top:1960px;height:630px;background:var(--band)}
.article{position:absolute;width:446px;height:198px;background:var(--white);box-shadow:0 2px 6px rgba(0,0,0,.15)}
.article-photo{position:absolute;left:0;top:0;width:227px;height:198px;background:linear-gradient(135deg,#cfd4d8,#6f7983)}
.date{position:absolute;left:199px;top:12px;width:43px;height:48px;background:var(--aqua);color:var(--white);text-align:center;font-size:19px;font-weight:600;line-height:24px;padding-top:2px}
.date small{display:block;font-size:11px;font-weight:400;line-height:14px}
.article h3{position:absolute;left:257px;top:14px;font-size:13.5px;font-weight:400;text-transform:uppercase;color:var(--ink)}
.article p{position:absolute;left:257px;top:42px;width:170px;font-size:12px;line-height:17px;color:var(--grey)}
.article .meta{position:absolute;left:257px;top:154px;display:flex;gap:14px;font-size:13px;font-weight:700;color:var(--ink);align-items:center}
.article .corner{position:absolute;right:0;bottom:0;width:0;height:0;border-left:22px solid transparent;border-bottom:22px solid var(--aqua)}

/* news */
.news{top:2590px;height:331px}
.news-item{position:absolute;top:162px;width:290px}
.cal{position:absolute;left:0;top:0;width:82px;height:84px}
.news-item h3{position:absolute;left:92px;top:2px;width:200px;font-size:13px;font-weight:400;line-height:18px;text-transform:uppercase;color:var(--ink)}
.news-item p{position:absolute;left:92px;top:42px;width:170px;font-size:12px;line-height:17px;color:var(--grey)}
.news-item a{position:absolute;left:92px;top:86px;font-size:11px;font-style:italic;color:var(--deep)}

/* memberships */
.memberships{top:2921px;height:290px;background:var(--band)}
.badge{position:absolute;top:152px;width:118px;height:77px;background:var(--white);display:flex;align-items:center;justify-content:center}
.badge span{display:block;width:76px;height:36px;border-radius:4px}

/* map */
.map{top:3211px;height:379px}
.map-area{position:absolute;inset:0;background:linear-gradient(135deg,#eaeae4,#dfe4dc 50%,#e8e6df)}
.map-card{position:absolute;left:637px;top:101px;width:196px;height:176px;background:var(--white);box-shadow:0 2px 8px rgba(0,0,0,.25);padding:12px 14px;font-size:11px;line-height:15px;color:var(--grey)}
.map-card strong{display:block;font-weight:600;color:var(--ink);text-transform:uppercase;margin-bottom:6px}
.map-card .row{display:flex;gap:7px;align-items:center;margin-top:8px}

/* footer */
.site-footer{top:3590px;height:32px;background:#2e9fd2;color:var(--white);font-size:11px;display:flex;align-items:center;justify-content:space-between;padding:0 145px}
.site-footer nav{display:flex;gap:8px;text-transform:uppercase}
</style>
</head>
<body>

<header class="site-header">
  <div class="abs brand"><span class="brand-dot"></span><span class="brand-name">Larkfield<br>Lawyers</span></div>
  <div class="abs top-info">
    <span><svg width="16" height="13" viewBox="0 0 16 13"><path d="M1 1h14v8H6l-3 3V9H1z" fill="var(--teal)"/></svg>Chat with Us</span>
    <span><svg width="15" height="11" viewBox="0 0 15 11"><rect x="0.5" y="0.5" width="14" height="10" fill="var(--teal)"/><path d="M1 1l6.5 5L14 1" stroke="#fff" fill="none"/></svg>info@larkfield.com</span>
    <span class="phone"><svg width="16" height="16" viewBox="0 0 16 16"><path d="M3 1l3 3-2 2c1 2 3 4 6 6l2-2 3 3-2 2C7 15 1 9 1 3z" fill="var(--teal)"/></svg>123.456.789</span>
  </div>
  <nav class="abs main-nav">
    <a class="current">Home</a><a>Who We Are</a><a>Services</a><a>Articles</a><a>Testimonials</a><a>Membership</a><a>Contact Us</a>
  </nav>
</header>

<section class="hero">
  <div class="hero-photo" role="img" aria-label="Photo of a group of young professionals smiling around a laptop"></div>
  <p class="hero-caption">Results driven, client focused lawyers<br>covering all areas of probate law</p>
</section>

<section class="who">
  <h2 class="section-title" style="top:42px">Who We Are</h2>
  <div class="title-rule" style="top:88px"></div>
  <p class="abs who-lead">Lorem Ipsum is simply dummy text of the printing and typesetting industry.</p>
  <div class="abs who-photo" role="img" aria-label="Photo of business people reviewing documents at a desk"></div>
  <p class="abs who-copy">Lorem ipsum dolor sit amet, consectetur adipiscing elit, sed do eiusmod tempor incididunt ut labore et dolore magna aliqua. Ut enim ad minim veniam, quis nostrud exercitation ullamco laboris nisi ut aliquip ex ea commodo consequat. Duis aute irure dolor in reprehenderit in voluptate velit esse cillum dolore eu fugiat nulla pariatur. Excepteur sint occaecat cupidatat non proident, sunt in culpa qui officia deserunt mollit anim id est laborum. Sed ut perspiciatis unde omnis iste natus error sit voluptatem accusantium doloremque laudantium, totam rem aperiam, eaque ipsa.</p>
  <span class="btn">READ MORE</span>
</section>

<section class="services on-band">
  <h2 class="section-title" style="top:44px">Our Services</h2>
  <div class="title-rule" style="top:90px"></div>
  <div class="service" style="left:142px">
    <div class="service-icon"><svg width="42" height="42" viewBox="0 0 42 42" fill="none" stroke="var(--aqua)" stroke-width="2.4"><path d="M10 20l11-9 11 9M14 17v10h14V17"/><path d="M4 33h10l6 3h12l6-5"/></svg></div>
    <h3>Property<br>Law</h3><p>Lorem ipsum dolor sit sit amet, consectetur adil eised diam nonummy</p>
  </div>
  <div class="service" style="left:325px">
    <div class="service-icon"><svg width="42" height="42" viewBox="0 0 42 42" fill="none" stroke="var(--aqua)" stroke-width="2.4"><rect x="9" y="6" width="20" height="28" rx="2"/><path d="M13 13h12M13 19h12M13 25h7M26 36l8-12 3 2-8 12z"/></svg></div>
    <h3>Wills</h3><p>Lorem ipsum dolor sit sit amet, consectetur adil eised diam nonummy</p>
  </div>
  <div class="service" style="left:511px">
    <div class="service-icon"><svg width="42" height="42" viewBox="0 0 42 42" fill="none" stroke="var(--aqua)" stroke-width="2.4"><rect x="10" y="5" width="22" height="32" rx="2"/><path d="M15 12h12M15 17h12"/><circle cx="21" cy="26" r="4"/><path d="M18 30l-1 5 4-2 4 2-1-5"/></svg></div>
    <h3>Powers of<br>Attorney</h3><p>Lorem ipsum dolor sit sit amet, consectetur adil eised diam nonummy</p>
  </div>
  <div class="service" style="left:695px">
    <div class="service-icon"><svg width="42" height="42" viewBox="0 0 42 42" fill="none" stroke="var(--aqua)" stroke-width="2.4"><rect x="8" y="5" width="24" height="32" rx="2"/><path d="M13 12h14M13 17h14M13 22h8"/><path d="M14 31l4-4 3 3 6-6"/></svg></div>
    <h3>Probate &amp; Estate<br>Administration</h3><p>Lorem ipsum dolor sit sit amet, consectetur adil eised diam nonummy</p>
  </div>
  <div class="service" style="left:880px">
    <div class="service-icon"><svg width="42" height="42" viewBox="0 0 42 42" fill="none" stroke="var(--aqua)" stroke-width="2.4"><rect x="6" y="6" width="30" height="22" rx="2"/><circle cx="16" cy="26" r="4"/><circle cx="27" cy="26" r="4"/><path d="M9 37c1-4 4-6 7-6s6 2 7 6M20 37c1-4 4-6 7-6s6 2 7 6"/></svg></div>
    <h3>Consultancy</h3><p>Lorem ipsum dolor sit sit amet, consectetur adil eised diam nonummy</p>
  </div>
</section>

<section class="testimonials">
  <h2 class="section-title" style="top:60px">Client Testimonials</h2>
  <div class="title-rule" style="top:106px"></div>
  <svg class="arrow" style="left:72px;top:258px" viewBox="0 0 30 54"><path d="M26 2L4 27l22 25" fill="none" stroke="#b5b5b5" stroke-width="3"/></svg>
  <svg class="arrow" style="left:1098px;top:258px" viewBox="0 0 30 54"><path d="M4 2l22 25L4 52" fill="none" stroke="#b5b5b5" stroke-width="3"/></svg>
  <div class="person" style="left:142px"><div class="avatar" role="img" aria-label="Client portrait"></div><h4>Miss Mara Quellen</h4></div>
  <div class="person" style="left:456px"><div class="avatar" role="img" aria-label="Client portrait"></div><h4>Miss Tavi Renholt</h4></div>
  <div class="person" style="left:770px"><div class="avatar" role="img" aria-label="Client portrait"></div><h4>Miss Odrin Vashel</h4></div>
  <div class="quote-card active" style="left:142px"><span class="qm">&ldquo;</span> Ut wisi enim ad minim veniam dole quisl mor nostrni exerci tation almet do ullamcorper suskcipit no lobortis norl nislk ut aliquip. <span class="qm">&rdquo;</span></div>
  <div class="quote-card" style="left:456px"><span class="qm">&ldquo;</span> Ut wisi enim ad minim veniam dole quisl mor nostrni exerci tation almet do ullamcorper suskcipit no lobortis norl nislk ut aliquip. <span class="qm">&rdquo;</span></div>
  <div class="quote-card" style="left:770px"><span class="qm">&ldquo;</span> Ut wisi enim ad minim veniam dole quisl mor nostrni exerci tation almet do ullamcorper suskcipit no lobortis norl nislk ut aliquip. <span class="qm">&rdquo;</span></div>
</section>

<section class="articles on-band">
  <h2 class="section-title" style="top:48px">Recent Articles</h2>
  <div class="title-rule" style="top:94px"></div>
  <svg class="arrow" style="left:72px;top:318px" viewBox="0 0 30 54"><path d="M26 2L4 27l22 25" fill="none" stroke="#fff" stroke-width="3"/></svg>
  <svg class="arrow" style="left:1098px;top:318px" viewBox="0 0 30 54"><path d="M4 2l22 25L4 52" fill="none" stroke="#fff" stroke-width="3"/></svg>

  <article class="article" style="left:142px;top:152px">
    <div class="article-photo" role="img" aria-label="Photo of colleagues shaking hands over a meeting table"></div>
    <div class="date">28<small>DEC</small></div>
    <h3>Lorem ipsum dolor</h3>
    <p>Lorem ipsum dolor sit do amet, etu adipiscing elit, sed diam nonum nibh do euismod tincidunt ut.</p>
    <div class="meta"><span>&#9901; 2</span><span>&lt; 0</span></div><span class="corner"></span>
  </article>
  <article class="article" style="left:611px;top:152px">
    <div class="article-photo" role="img" aria-label="Photo of a hand signing a document"></div>
    <div class="date">29<small>DEC</small></div>
    <h3>Lorem ipsum dolor</h3>
    <p>Lorem ipsum dolor sit do amet, etu adipiscing elit, sed diam nonum nibh do euismod tincidunt ut.</p>
    <div class="meta"><span>&#9901; 2</span><span>&lt; 0</span></div><span class="corner"></span>
  </article>
  <article class="article" style="left:142px;top:367px">
    <div class="article-photo" role="img" aria-label="Photo of a businessman on a phone call"></div>
    <div class="date">30<small>DEC</small></div>
    <h3>Lorem ipsum dolor</h3>
    <p>Lorem ipsum dolor sit do amet, etu adipiscing elit, sed diam nonum nibh do euismod tincidunt ut.</p>
    <div class="meta"><span>&#9901; 2</span><span>&lt; 0</span></div><span class="corner"></span>
  </article>
  <article class="article" style="left:611px;top:367px">
    <div class="article-photo" role="img" aria-label="Photo of a client consultation across a desk"></div>
    <div class="date">31<small>DEC</small></div>
    <h3>Lorem ipsum dolor</h3>
    <p>Lorem ipsum dolor sit do amet, etu adipiscing elit, sed diam nonum nibh do euismod tincidunt ut.</p>
    <div class="meta"><span>&#9901; 2</span><span>&lt; 0</span></div><span class="corner"></span>
  </article>
</section>

<section class="news">
  <h2 class="section-title" style="top:60px">Recent News</h2>
  <div class="title-rule" style="top:106px"></div>
  <svg class="arrow" style="left:72px;top:188px" viewBox="0 0 30 54"><path d="M26 2L4 27l22 25" fill="none" stroke="#b5b5b5" stroke-width="3"/></svg>
  <svg class="arrow" style="left:1098px;top:188px" viewBox="0 0 30 54"><path d="M4 2l22 25L4 52" fill="none" stroke="#b5b5b5" stroke-width="3"/></svg>

  <div class="news-item" style="left:142px">
    <svg class="cal" viewBox="0 0 82 84"><rect x="3" y="10" width="76" height="71" rx="6" fill="#fff" stroke="var(--blue)" stroke-width="5"/><rect x="3" y="10" width="76" height="18" fill="var(--blue)"/><rect x="20" y="2" width="6" height="16" rx="3" fill="var(--blue)"/><rect x="56" y="2" width="6" height="16" rx="3" fill="var(--blue)"/><text x="41" y="55" text-anchor="middle" font-family="Open Sans,sans-serif" font-size="18" fill="#333">02<tspan font-size="10" dy="-6">th</tspan></text><text x="41" y="72" text-anchor="middle" font-family="Open Sans,sans-serif" font-size="14" fill="#333">JAN</text></svg>
    <h3>Lorem ipsum dolor sit am ewectetuer</h3><p>Lorem ipsum dolor sit amet, consec ingrer</p><a>Read More</a>
  </div>
  <div class="news-item" style="left:471px">
    <svg class="cal" viewBox="0 0 82 84"><rect x="3" y="10" width="76" height="71" rx="6" fill="#fff" stroke="var(--blue)" stroke-width="5"/><rect x="3" y="10" width="76" height="18" fill="var(--blue)"/><rect x="20" y="2" width="6" height="16" rx="3" fill="var(--blue)"/><rect x="56" y="2" width="6" height="16" rx="3" fill="var(--blue)"/><text x="41" y="55" text-anchor="middle" font-family="Open Sans,sans-serif" font-size="18" fill="#333">03<tspan font-size="10" dy="-6">th</tspan></text><text x="41" y="72" text-anchor="middle" font-family="Open Sans,sans-serif" font-size="14" fill="#333">JAN</text></svg>
    <h3>Lorem ipsum dolor sit am ewectetuer</h3><p>Lorem ipsum dolor sit amet, consec ingrer</p><a>Read More</a>
  </div>
  <div class="news-item" style="left:799px">
    <svg class="cal" viewBox="0 0 82 84"><rect x="3" y="10" width="76" height="71" rx="6" fill="#fff" stroke="var(--blue)" stroke-width="5"/><rect x="3" y="10" width="76" height="18" fill="var(--blue)"/><rect x="20" y="2" width="6" height="16" rx="3" fill="var(--blue)"/><rect x="56" y="2" width="6" height="16" rx="3" fill="var(--blue)"/><text x="41" y="55" text-anchor="middle" font-family="Open Sans,sans-serif" font-size="18" fill="#333">05<tspan font-size="10" dy="-6">th</tspan></text><text x="41" y="72" text-anchor="middle" font-family="Open Sans,sans-serif" font-size="14" fill="#333">JAN</text></svg>
    <h3>Lorem ipsum dolor sit am ewectetuer</h3><p>Lorem ipsum dolor sit amet, consec ingrer</p><a>Read More</a>
  </div>
</section>

<section class="memberships on-band">
  <h2 class="section-title" style="top:48px">Our Memberships</h2>
  <div class="title-rule" style="top:94px"></div>
  <div class="badge" style="left:142px" role="img" aria-label="KRT Member badge"><span style="background:#7a4a8c"></span></div>
  <div class="badge" style="left:274px" role="img" aria-label="Coastal Female Advocates badge"><span style="background:#9a3d6a"></span></div>
  <div class="badge" style="left:407px" role="img" aria-label="Guides From Counsel badge"><span style="background:#e8872c"></span></div>
  <div class="badge" style="left:540px" role="img" aria-label="Creature Foundation badge"><span style="background:#2f6fb5"></span></div>
  <div class="badge" style="left:673px" role="img" aria-label="Dorvo badge"><span style="background:#6b3a8c"></span></div>
  <div class="badge" style="left:806px" role="img" aria-label="Malpeth badge"><span style="background:#d3262f"></span></div>
  <div class="badge" style="left:939px" role="img" aria-label="Kel QR badge"><span style="background:#8cc63f"></span></div>
</section>

<section class="map">
  <div class="map-area" role="img" aria-label="Street map showing the office location"></div>
  <svg class="abs" style="left:586px;top:140px" width="28" height="40" viewBox="0 0 28 40"><path d="M14 1C7 1 1 6.5 1 14c0 9 13 25 13 25s13-16 13-25C27 6.5 21 1 14 1z" fill="var(--aqua)"/><circle cx="14" cy="14" r="5" fill="#fff"/></svg>
  <div class="map-card">
    <strong>Larkfield Lawyers</strong>
    <div class="row"><svg width="10" height="14" viewBox="0 0 10 14"><path d="M5 0C2 0 0 2 0 5c0 3 5 9 5 9s5-6 5-9c0-3-2-5-5-5z" fill="var(--aqua)"/></svg><span>123 Lorem Ipsum, Suite 138 Biert nweet, consec ingrer AB 12345</span></div>
    <div class="row"><svg width="11" height="11" viewBox="0 0 16 16"><path d="M3 1l3 3-2 2c1 2 3 4 6 6l2-2 3 3-2 2C7 15 1 9 1 3z" fill="var(--aqua)"/></svg>(123) 456-7890</div>
    <div class="row"><svg width="11" height="11" viewBox="0 0 16 16"><rect x="1" y="3" width="14" height="10" fill="var(--aqua)"/></svg>(123) 456-7890</div>
    <div class="row"><svg width="11" height="9" viewBox="0 0 15 11"><rect x="0.5" y="0.5" width="14" height="10" fill="var(--aqua)"/><path d="M1 1l6.5 5L14 1" stroke="#fff" fill="none"/></svg>info@larkfieldlawyers.com</div>
  </div>
</section>

<footer class="site-footer">
  <nav><span>Home</span>|<span>Who We Are</span>|<span>Our Services</span>|<span>Articles</span>|<span>Contact Us</span></nav>
  <span>Copyright &copy; 2018 Larkfield Lawyers. All Rights Reserved.</span>
</footer>

</body>
</html>
```